Brightmoor Pathways

We need a website designed for a life coaching company who specialises in one on one coaching, workshops and seminars where they teach participants in goal setting and how to achieve them for a better life.

Objectives

·         Easy to use

·         Clear & concise

·         Quality but not too flashy

·         Shows clearly what you do and how you interact with clients

·         No fuss, straight up

·         Gives those who hear your name or business name a place to go to obtain further information on what I am doing, why & how they can use my services.

·         A way for clients to contact you

·         Seminar & workshop bookings (not mandatory)

·         Most of the website to be static.

Number of Pages Required

1 page

Requirements
Must have
• Sitemap

• Home
• About Us
• One on One Coaching
• Workshops/Seminars
• How we Work?
• Pricing
• Testimonials
• Contact Us

• Design/Content Brief

• ü  The following elements are included in the design/content brief which this proposal is based on:

• o    Flash banner with some images rotating that reflect your business.

• o    Logo and phone number 0438 760 214 will be prominently displayed.

• o    Horizontal Navigation

• o    Contact Us icon on homepage

• o    Sign up for our newsletter on homepage

• o    Privacy Policy/Sitemap/Terms & Conditions in footer

• o    - larger rounded buttons

• o    - good size font

• o    - not having to scroll too far

• o    - soft feel, but not fluffy (images will enhance this)

• ü  Colours that could be used with logo

• o   What about this?  RGB 128,128,128

• o   What about this?  RGB 54, 95, 145

• o   What about this?  RGB 51, 204, 51

• o   Red – R255

• ü   http://www.plumvexlo.com/

• o    I like this website and its rounded buttons, large easy to see and use.

• o    Soft colours

• o    Changing pictures at the top of screen

• Files

```html
<!DOCTYPE html>
<html lang="en">
<head>
<meta charset="utf-8">
<title>Brightmoor Pathways</title>
<link rel="stylesheet" href="https://fonts.googleapis.com/css2?family=Noto+Sans:wght@400;700&family=PT+Serif:wght@700&display=swap">
<style>
:root{
  --stage:#cfcac4;
  --paper:#ffffff;
  --red:#e0201c;
  --red-mid:#d0231f;
  --red-deep:#a82226;
  --ink:#1c1c1c;
  --panel:#cfcac4;
  --field:#dcd8d2;
}
*{box-sizing:border-box;margin:0;padding:0}
html,body{width:1200px;height:1197px;overflow:hidden}
body{background:var(--stage);font-family:"Noto Sans",sans-serif;color:var(--ink);position:relative}
.page{position:absolute;left:120px;top:141px;width:960px;height:915px;background:var(--paper);border-radius:0 0 30px 30px;overflow:hidden}
.callout{position:absolute;left:764px;top:1px;width:127px;height:39px;background:linear-gradient(var(--red),var(--red-deep));border-radius:0 0 8px 8px;color:#fff;text-align:center;padding-top:5px}
.callout small{display:block;font-size:11px;line-height:12px}
.callout strong{display:block;font-weight:400;font-size:16px;line-height:18px;letter-spacing:.5px}
.account{position:absolute;left:764px;top:73px;width:127px;height:44px;background:linear-gradient(var(--red),var(--red-mid));border-radius:9px 9px 0 0;color:#fff;font-size:17px;text-align:center;padding-top:10px}
.brand{position:absolute;left:72px;top:50px;display:flex;align-items:center;gap:10px;color:var(--red);font-family:"PT Serif",serif;font-weight:700;font-size:24px;letter-spacing:2px}
.brand i{width:16px;height:16px;border-radius:50%;background:var(--red);display:block}
.banner{position:absolute;left:54px;top:112px;width:851px;height:191px;border-radius:11px;background:linear-gradient(170deg,#c9754f 0%,#e0643c 35%,#8a4a44 65%,#d45a38 100%)}
.nav{position:absolute;left:54px;top:320px;display:flex;gap:4px;list-style:none}
.nav li{width:103px;height:37px;border-radius:7px;background:linear-gradient(var(--red),var(--red-deep));color:#fff;font-size:12px;line-height:14px;display:flex;align-items:center;justify-content:center;text-align:center;box-shadow:inset 0 1px 0 rgba(255,255,255,.35)}
.content{position:absolute;left:15px;top:373px;width:930px;height:373px;background:var(--panel)}
.content h1{position:absolute;left:50px;top:24px;font-size:14px;font-variant:small-caps;letter-spacing:.8px}
.content p{position:absolute;left:50px;font-size:11.3px;line-height:14.2px;text-align:justify;letter-spacing:.2px}
.lead{top:51px;width:814px}
.body-a{top:138px;width:627px}
.body-b{top:252px;width:627px}
.newsletter{position:absolute;left:833px;top:637px;width:200px;height:199px;border-radius:13px;background:var(--red-mid);padding:5px;border:2px solid var(--red-deep)}
.newsletter-inner{height:100%;border-radius:10px;background:linear-gradient(#d8302a,#b3242a 85%,#d66 100%);text-align:center;color:#fff;padding-top:10px}
.newsletter h2{font-size:16px;line-height:17px;font-weight:700}
.field{width:164px;height:24px;margin:6px auto 0;background:var(--field);color:#333;font-size:10px;line-height:24px}
.field:first-of-type{margin-top:6px}
.submit{width:75px;height:17px;margin:8px auto 0;border-radius:9px;background:#fff;color:var(--red);font-size:12px;font-weight:700;line-height:17px;letter-spacing:.5px}
.newsletter-note{font-size:9.5px;line-height:11px;margin-top:9px;padding:0 24px;text-align:left}
.footer{position:absolute;left:0;top:801px;width:960px;height:114px;background:linear-gradient(90deg,var(--red),var(--red-deep))}
.footer svg{position:absolute;left:0;top:0}
.footer-name{position:absolute;left:60px;top:3px;color:var(--red);font-family:"PT Serif",serif;font-weight:700;font-size:23px;letter-spacing:3px}
.footer-rule{position:absolute;left:54px;top:33px;width:295px;height:5px;background:var(--red)}
.legal{position:absolute;left:627px;top:63px;color:#fff;font-size:12px;line-height:16px;letter-spacing:.2px}
.legal span{color:#2a0c0c}
</style>
</head>
<body>
<div class="page">
  <div class="callout"><small>Need Help? Call Now!</small><strong>0438 760 214</strong></div>
  <div class="brand"><i></i>Brightmoor Pathways</div>
  <div class="account">login | join</div>
  <div class="banner" role="img" aria-label="Banner photo of a person raising both arms against a red sunset sky"></div>
  <ul class="nav">
    <li>| Home</li><li>| About Us</li><li>| One on One<br>Coaching</li><li>| Workshops<br>Seminars</li><li>| How we<br>Work?</li><li>| Pricing</li><li>| Testimonials</li><li>| Contact Us</li>
  </ul>
  <section class="content">
    <h1>Lorem ipsum dolor</h1>
    <p class="lead">Lorem ipsum dolor sit amet, consetetur sadipscing elitr, sed diam nonumy eirmod tempor invidunt ut labore et dolore magna aliquyam erat, sed diam voluptua. At vero eos et accusam et justo duo dolores et ea rebum. Stet clita kasd gubergren, no sea takimata sanctus est Lorem ipsum dolor sit amet. Lorem ipsum dolor sit amet, consetetur sadipscing elitr, sed diam nonumy eirmod tempor invidunt ut labore et dolore magna aliquyam erat, sed diam voluptua. At vero eos et accusam et justo duo dolores et ea rebum. Stet clita kasd gubergren, no sea takimata sanctus est Lorem ipsum dolor sit amet. Lorem ipsum dolor sit amet.</p>
    <p class="body-a">Lorem ipsum dolor sit amet, consetetur sadipscing elitr, sed diam nonumy eirmod tempor invidunt ut labore et dolore magna aliquyam erat, sed diam voluptua. At vero eos et accusam et justo duo dolores et ea rebum. Stet clita kasd gubergren, no sea takimata sanctus est Lorem ipsum dolor sit amet. Lorem ipsum dolor sit amet, consetetur sadipscing elitr, sed diam nonumy eirmod tempor invidunt ut labore et dolore magna aliquyam erat, sed diam voluptua.At vero eos et accusam et justo duo dolores et ea rebum. Stet clita kasd gubergren, no sea takimata sanctus est Lorem ipsum dolor sit amet. Lorem ipsum dolor sit amet.</p>
    <p class="body-b">Lorem ipsum dolor sit amet, consetetur sadipscing elitr, sed diam nonumy eirmod tempor invidunt ut labore et dolore magna aliquyam erat, sed diam voluptua. At vero eos et accusam et justo duo dolores et ea rebum. Stet clita kasd gubergren, no sea takimata sanctus est Lorem ipsum dolor sit amet. Lorem ipsum dolor sit amet, consetetur sadipscing elitr, sed diam nonumy eirmod tempor invidunt ut labore et dolore magna aliquyam erat, sed diam voluptua.At vero eos et accusam et justo duo dolores et ea rebum. Stet clita kasd gubergren, no sea takimata sanctus est Lorem ipsum dolor sit amet. Lorem ipsum dolor sit amet.</p>
  </section>
  <footer class="footer">
    <svg width="362" height="50" viewBox="0 0 362 50"><polygon points="0,0 362,0 362,49 41,49" fill="#ffffff"/></svg>
    <div class="footer-name">Brightmoor Pathways</div>
    <div class="footer-rule"></div>
    <div class="legal">Privacy Policy | Sitemap | Terms &amp; Conditions<br><span>Copyright Brightmoor Pathways</span> | All Rights Reserved</div>
  </footer>
</div>
<aside class="newsletter">
  <div class="newsletter-inner">
    <h2>Sign Up for our<br>Newsletter</h2>
    <div class="field">Type In Your Name</div>
    <div class="field">Type In Your Email</div>
    <div class="submit">SUBMIT</div>
    <div class="newsletter-note">Lorem ipsum dolor sit amet, consetetur sadipscing elitr, sed diam nonumy eirmod</div>
  </div>
</aside>
</body>
</html>
```